First Aid Training business needs business card design

We would like a double sided business card designed for a first aid training business - Brindlewood First Aid. We provide first aid training and , WHS (work, health and safety) training.

The attached word document contains the key information we would like on each side of the business card.

Final design needs to be delivered in print ready format, along with the original file.

```html
<!DOCTYPE html>
<html lang="en">
<head>
<meta charset="utf-8">
<title>Brindlewood First Aid – Business Card</title>
<link href="https://fonts.googleapis.com/css2?family=Josefin+Sans:wght@300;400;700&display=swap" rel="stylesheet">
<style>
  :root {
    --backdrop: #d7d7d7;
    --paper: #ffffff;
    --brand-red: #e3211f;
    --ink: #111111;
    --rule-grey: #9a9a9a;
    --stripe-grey: #8c8c8c;
    --art-red-light: #f0474a;
    --art-red-dark: #c41c1f;
  }
  * { box-sizing: border-box; margin: 0; padding: 0; }
  html, body {
    width: 1200px; height: 846px; overflow: hidden;
    background: var(--backdrop);
    font-family: "Josefin Sans", sans-serif;
    color: var(--ink);
  }
  .sheet {
    width: 1200px; height: 846px;
    display: flex; align-items: center; justify-content: center; gap: 40px;
  }
  .card {
    position: relative;
    width: 540px; height: 330px;
    background: var(--paper);
    overflow: hidden;
    box-shadow: 0 6px 18px rgba(0,0,0,0.18);
  }

  /* Front side */
  .brand {
    position: absolute; left: 28px; top: 118px;
    width: 222px;
    display: flex; align-items: center; gap: 10px;
  }
  .brand__dot {
    width: 34px; height: 34px; border-radius: 50%;
    background: var(--brand-red); flex: none;
  }
  .brand__name {
    font-weight: 700; font-size: 20px; line-height: 1.1;
    color: var(--ink); text-transform: uppercase; letter-spacing: 0.3px;
    white-space: nowrap;
  }
  .divider {
    position: absolute; left: 262px; top: 118px;
    width: 1px; height: 92px; background: var(--rule-grey);
  }
  .person {
    position: absolute; left: 278px; top: 66px;
    font-weight: 700; font-size: 24px; letter-spacing: 0.5px;
    text-transform: uppercase; white-space: nowrap;
  }
  .person__surname { color: var(--brand-red); }
  .contacts {
    position: absolute; left: 278px; top: 122px;
    list-style: none;
    font-weight: 300; font-size: 14px;
  }
  .contacts li {
    display: flex; align-items: center; gap: 8px;
    height: 26px; white-space: nowrap;
  }
  .contacts svg { width: 13px; height: 13px; flex: none; }
  .stripes { position: absolute; left: 0; right: 0; bottom: 0; }
  .stripes__grey { height: 4px; background: var(--stripe-grey); }
  .stripes__black { height: 10px; background: var(--ink); }
  .stripes__gap { height: 4px; background: var(--paper); }
  .stripes__red { height: 45px; background: var(--brand-red); }

  /* Back side */
  .mascot-art {
    position: absolute; left: 24px; top: 70px;
    width: 240px; height: 250px;
    background: radial-gradient(closest-side, var(--art-red-light) 0%, var(--art-red-dark) 70%, rgba(196,28,31,0) 100%);
  }
  .pitch {
    position: absolute; right: 28px; top: 44px;
    text-align: right;
  }
  .pitch__title {
    font-weight: 700; font-size: 31px; color: var(--brand-red);
    line-height: 1.1;
  }
  .pitch__subtitle {
    font-weight: 700; font-size: 18px; line-height: 1.3;
  }
  .benefits {
    list-style: none; margin-top: 18px;
    font-weight: 300; font-size: 15.5px; line-height: 1.5;
  }
  .benefits__bullet { color: var(--brand-red); font-weight: 700; margin-left: 4px; }
  .services {
    position: absolute; right: 28px; bottom: 28px;
    font-weight: 300; font-size: 16px; white-space: nowrap;
  }
</style>
</head>
<body>
  <main class="sheet">
    <section class="card card--front" aria-label="Business card front">
      <div class="brand">
        <span class="brand__dot"></span>
        <span class="brand__name">Brindlewood<br>First Aid</span>
      </div>
      <div class="divider"></div>
      <h1 class="person">Daniel <span class="person__surname">Hartley</span></h1>
      <ul class="contacts">
        <li>
          <svg viewBox="0 0 16 16" aria-hidden="true"><path fill="var(--brand-red)" d="M4 1.5l2.2 3-1.3 1.6c.8 1.9 2.2 3.4 4.1 4.2l1.5-1.3 3 2.2-1.3 2.8C6.8 13.6 2.3 9.1 1.3 3.4z"/></svg>
          0412 555 038
        </li>
        <li>
          <svg viewBox="0 0 16 16" aria-hidden="true"><rect x="1" y="3" width="14" height="10" fill="var(--brand-red)"/><path d="M1.5 3.5L8 9l6.5-5.5" fill="none" stroke="#fff" stroke-width="1.3"/></svg>
          help@brindlewoodfirstaid.com.au
        </li>
        <li>
          <svg viewBox="0 0 16 16" aria-hidden="true"><circle cx="8" cy="8" r="6.5" fill="none" stroke="var(--brand-red)" stroke-width="1.6"/><ellipse cx="8" cy="8" rx="2.8" ry="6.5" fill="none" stroke="var(--brand-red)" stroke-width="1.2"/><path d="M1.5 8h13M2.6 4.8h10.8M2.6 11.2h10.8" stroke="var(--brand-red)" stroke-width="1.1"/></svg>
          www.brindlewoodfirstaid.com.au
        </li>
      </ul>
      <div class="stripes" aria-hidden="true">
        <div class="stripes__grey"></div>
        <div class="stripes__black"></div>
        <div class="stripes__gap"></div>
        <div class="stripes__red"></div>
      </div>
    </section>

    <section class="card card--back" aria-label="Business card back">
      <div class="mascot-art" role="img" aria-label="Illustration of a red first aid kit mascot walking and carrying a small first aid case"></div>
      <div class="pitch">
        <h2 class="pitch__title">Onsite Training</h2>
        <p class="pitch__subtitle">- We can come to you</p>
        <ul class="benefits">
          <li>Time efficient<span class="benefits__bullet">•</span></li>
          <li>Cost effective<span class="benefits__bullet">•</span></li>
          <li>Minimise downtime<span class="benefits__bullet">•</span></li>
          <li>for your team&nbsp;&nbsp;</li>
        </ul>
      </div>
      <p class="services">First Aid Training &amp; WHS Training</p>
    </section>
  </main>
</body>
</html>
```